Business Card Design Project Lumaro Foundation

Looking for business card options to match our concurrent logo project on sketch forge. We are a international humanitarian aid firm. We work in the non profit sector but operate more closely to a traditional for-profit investment firm. As such we would like equal tones in our branding materials, which includes are business cards.

Stand by for logo...
Updates

logo uploaded.

Target Market(s)

Adults in western speaking countries ages 18-40 that work primarily in the NGO and Business Administrative Career Field.

Industry/Entity Type

Non Profit

Font styles to use
Sans Serif

Requirements
Nice to have
• We would like all contact information on one side.

Company Name/Logo, Individual Name and Position on the other...

```html
<!DOCTYPE html>
<html lang="en">
<head>
<meta charset="utf-8">
<title>Lumaro Foundation — Business Card</title>
<link rel="stylesheet" href="https://fonts.googleapis.com/css2?family=Poppins:wght@400;600;700&display=swap">
<style>
  :root {
    --backdrop: #dedfe1;
    --card: #f1f1f2;
    --card-front: #f4f4f5;
    --sky: #93bfd8;
    --sage: #c3d5b0;
    --stone: #cfd0d3;
    --navy-top: #4252ad;
    --navy-bottom: #26388a;
    --ink: #1c1c1f;
    --charcoal: #4a4a4f;
    --violet: #3d46a3;
    --leaf: #7fb04a;
  }
  * { box-sizing: border-box; margin: 0; padding: 0; }
  html, body {
    width: 1200px; height: 1200px; overflow: hidden;
    background: var(--backdrop);
    font-family: "Poppins", sans-serif;
  }
  .canvas { position: relative; width: 1200px; height: 1200px; }
  .card {
    position: absolute; left: 250px; width: 700px; height: 400px;
    overflow: hidden; border-radius: 4px;
    box-shadow: 0 10px 30px rgba(0,0,0,0.12);
  }
  .card--front { top: 130px; background: var(--card-front); }
  .card--contact { top: 670px; background: var(--card); }
  .card svg.shapes { position: absolute; inset: 0; }

  .wordmark {
    position: absolute; display: flex; align-items: center; gap: 16px;
    font-weight: 600; white-space: nowrap;
  }
  .wordmark__dot { display: block; background: currentColor; }
  .card--front .wordmark {
    left: 110px; top: 218px; color: var(--charcoal);
    font-size: 44px; letter-spacing: 4px;
  }
  .card--front .wordmark__dot { width: 44px; height: 44px; }
  .card--contact .wordmark {
    left: 36px; top: 344px; color: #ffffff;
    font-size: 20px; letter-spacing: 2px; gap: 10px;
  }
  .card--contact .wordmark__dot { width: 20px; height: 20px; }

  .person { position: absolute; left: 420px; top: 168px; }
  .person__name { font-weight: 700; font-size: 30px; color: var(--ink); line-height: 1.1; }
  .person__role { font-weight: 400; font-size: 17px; color: var(--violet); }

  .contact {
    position: absolute; left: 40px; top: 252px;
    display: flex; align-items: center; gap: 24px;
    color: var(--violet); font-size: 19px; line-height: 1.45;
  }
  .contact__list { list-style: none; }
  .contact__list li { display: flex; align-items: center; gap: 8px; }
  .contact__icon {
    width: 11px; height: 11px; border-radius: 50%;
    border: 2px solid var(--leaf); flex: none;
  }
  .contact__divider { width: 2px; height: 44px; background: var(--leaf); }
</style>
</head>
<body>
<main class="canvas">

  <section class="card card--front" aria-label="Card front">
    <svg class="shapes" width="700" height="400" viewBox="0 0 700 400" aria-hidden="true">
      <polygon points="470,0 560,0 560,60 520,100 470,100" fill="var(--sky)"/>
      <polygon points="575,0 700,0 700,70 640,110 560,110 560,80 590,40" fill="var(--stone)"/>
      <polygon points="450,120 545,120 610,150 700,100 700,140 620,190 450,190" fill="var(--sage)"/>
    </svg>
    <div class="wordmark"><span class="wordmark__dot"></span>Lumaro Foundation</div>
  </section>

  <section class="card card--contact" aria-label="Card back with contact details">
    <svg class="shapes" width="700" height="400" viewBox="0 0 700 400" aria-hidden="true">
      <defs>
        <linearGradient id="navyBand" x1="0" y1="0" x2="1" y2="0">
          <stop offset="0" stop-color="var(--navy-bottom)"/>
          <stop offset="1" stop-color="var(--navy-top)"/>
        </linearGradient>
      </defs>
      <polygon points="0,0 200,0 200,200 0,200" fill="var(--sage)"/>
      <polygon points="218,0 375,0 375,180 430,240 700,240 700,300 400,300 330,235 218,235" fill="var(--stone)"/>
      <polygon points="393,0 700,0 700,180 650,222 445,222 393,165" fill="var(--sky)"/>
      <rect x="0" y="322" width="700" height="78" fill="url(#navyBand)"/>
    </svg>

    <div class="person">
      <p class="person__name">Alden Marsh</p>
      <p class="person__role">President</p>
    </div>

    <div class="contact">
      <ul class="contact__list">
        <li>555 555 555</li>
        <li>555 555 556</li>
      </ul>
      <span class="contact__divider"></span>
      <ul class="contact__list">
        <li><span class="contact__icon"></span>www.website.com</li>
        <li><span class="contact__icon"></span>email@email.com</li>
      </ul>
    </div>

    <div class="wordmark"><span class="wordmark__dot"></span>Lumaro Foundation</div>
  </section>

</main>
</body>
</html>
```